Audio Visual company needs brochure design

We are an AV company that does Audio Visual work solely for Commercial customers. We Design, sale and install various Audio Visual systems for our customers. This may be something as simple as a conference room, a new sound system for a church or a new sound, lighting and video system for an arena or stadium.

We don't really have any ideas in mind and that's the reason we are turning to you. We want something that highlights what we do, and something they will look at - not just toss in the can.

Included is a copy of our logo (sorry it's the only copy we have now)

Our company name is Velmira Staging www.velmirastaging.example
Updates

Reason: The rest of our management team hasn't provided feedback to me yet. We will pick the design this week.

Target Market(s)

70% of our business is churches and the remaining is corporate customers and restaurants.

Industry/Entity Type

Church

Requirements
Must have
• The brochure will be 8.5" x 11" printed both sides - open to Z fold or Tri fold designs. We can provide pictures of our work if needed - though they may not be the best.
Should not have
• No generic pictures of just speakers, projectors, microphones, etc.

```html
<!DOCTYPE html>
<html lang="en">
<head>
<meta charset="utf-8">
<title>Velmira Staging – Sound &amp; Lighting Brochure</title>
<link href="https://fonts.googleapis.com/css2?family=Roboto+Condensed:wght@500&family=Open+Sans:wght@400&display=swap" rel="stylesheet">
<style>
  :root {
    --sky-blue: #7b9bfa;
    --pale-blue: #d5ddfb;
    --paper: #ffffff;
    --ink: #111111;
    --rule: #3a3a3a;
    --photo-warm: #8a6a4a;
    --photo-dark: #3b332c;
    --photo-red: #a8483f;
  }
  html, body {
    margin: 0;
    padding: 0;
    width: 1200px;
    height: 928px;
    overflow: hidden;
    background: var(--paper);
  }
  .brochure {
    position: relative;
    width: 1200px;
    height: 928px;
    overflow: hidden;
    background: var(--paper);
  }
  .backdrop {
    position: absolute;
    inset: 0;
    width: 1200px;
    height: 928px;
  }
  .panel-heading {
    position: absolute;
    margin: 0;
    font-family: "Roboto Condensed", "Arial Narrow", sans-serif;
    font-weight: 500;
    color: var(--paper);
    font-size: 47px;
    line-height: 58px;
  }
  .heading-church { left: 26px; top: 46px; }
  .heading-events { left: 400px; width: 400px; top: 82px; text-align: center; line-height: 60px; }
  .heading-systems { left: 851px; top: 210px; line-height: 60px; }
  .panel-copy {
    position: absolute;
    margin: 0;
    font-family: "Open Sans", Arial, sans-serif;
    font-size: 21px;
    line-height: 29.5px;
    color: var(--ink);
  }
  .panel-copy p { margin: 0 0 29.5px; }
  .copy-church { left: 13px; top: 616px; width: 385px; }
  .copy-events { left: 411px; top: 616px; width: 385px; }
  .copy-systems { left: 808px; top: 830px; width: 390px; }
</style>
</head>
<body>
<main class="brochure">
  <svg class="backdrop" viewBox="0 0 1300 1005" preserveAspectRatio="none" aria-hidden="false">
    <defs>
      <linearGradient id="church-interior" x1="0" y1="0" x2="0" y2="1">
        <stop offset="0" stop-color="#e8e4dc"/>
        <stop offset="0.55" stop-color="var(--photo-warm)"/>
        <stop offset="1" stop-color="var(--photo-dark)"/>
      </linearGradient>
      <linearGradient id="mixing-desk" x1="0" y1="0" x2="0" y2="1">
        <stop offset="0" stop-color="#e9e2d6"/>
        <stop offset="0.5" stop-color="#9a8a78"/>
        <stop offset="1" stop-color="#2a2623"/>
      </linearGradient>
      <linearGradient id="church-foyer" x1="0" y1="0" x2="0" y2="1">
        <stop offset="0" stop-color="#efe9e2"/>
        <stop offset="0.35" stop-color="var(--photo-red)"/>
        <stop offset="0.6" stop-color="#d9d4cc"/>
        <stop offset="1" stop-color="#7a6a55"/>
      </linearGradient>
    </defs>

    <path class="pale-band" fill="var(--pale-blue)"
      d="M0,0 H1300 V1005 H1290 C1200,930 1020,760 866,700 C700,560 560,470 433,470 C300,470 150,480 0,500 Z"/>
    <path class="sky-band" fill="var(--sky-blue)"
      d="M0,0 H1300 V870 C1200,800 1020,620 866,535 C700,440 560,385 433,385 C300,385 150,360 0,380 Z"/>

    <line class="fold-line" x1="433.5" y1="0" x2="433.5" y2="1005" stroke="var(--rule)" stroke-width="1.2"/>
    <line class="fold-line" x1="866.5" y1="0" x2="866.5" y2="1005" stroke="var(--rule)" stroke-width="1.2"/>

    <g class="photo photo-church" role="img" aria-label="Photo of a church sanctuary with rows of chairs, a cross on the front wall and two projection screens">
      <circle cx="225" cy="410" r="196" fill="var(--pale-blue)"/>
      <circle cx="225" cy="410" r="187" fill="url(#church-interior)"/>
    </g>
    <g class="photo photo-desk" role="img" aria-label="Photo of a digital mixing console and equipment rack in a sound booth">
      <circle cx="650" cy="488" r="170" fill="var(--pale-blue)"/>
      <circle cx="650" cy="488" r="161" fill="url(#mixing-desk)"/>
    </g>
    <g class="photo photo-foyer" role="img" aria-label="Photo of a church hall with a red gable wall, stained glass windows and glass doors">
      <circle cx="1085" cy="680" r="152" fill="var(--pale-blue)"/>
      <circle cx="1085" cy="680" r="143" fill="url(#church-foyer)"/>
    </g>
  </svg>

  <h2 class="panel-heading heading-church">Sound &amp; Lighting<br>System in Church</h2>
  <h2 class="panel-heading heading-events">Audio Systems<br>for<br>Events</h2>
  <h2 class="panel-heading heading-systems">Our perfect<br>Lighting &amp;<br>Sound Systems</h2>

  <div class="panel-copy copy-church">
    <p>We specialize in all aspects of sound reinforcement, lighting, video and staging systems in both the installation and production markets.</p>
    <p>In business today, execution of the &nbsp;details can mean the difference between success and failure. A poorly designed and installed system can be a disaster if it fails at the wrong time.</p>
  </div>
  <div class="panel-copy copy-events">
    <p>A poorly planned event or convention could result in disaster for your company's image. We know that cost control is extremely important when it comes to projecting a positive image and building a powerful message.</p>
    <p>Our experienced crew has the tools needed to bring you to the next level</p>
  </div>
  <div class="panel-copy copy-systems">
    <p>while maintaining a cost effective goal. Using fresh innovated ideas, you wont find cookie cutter services here.</p>
  </div>
</main>
</body>
</html>
```